Hallvard
Veneer Technology
Hallvard - Agriculture
Creative Brief
Agriculture
http://hallvard-veneertechnology.example
We have 4 different product lines.
1. Stone-Veneer
2.Sonic-Paneltrim
3.Plexard
4.Moravelt
We do not installl any products. We just distribute them to architects, companies, builders, ect.
The stone can be made for any products. From laptops, countertops, "wall paper", notebooks, smart car, sinks, ect.
Dislikes: -it's hard to see what our company is -appearance -professionalism -pictures -it's not appealing
Nature
Gray, white and blacks
Blues
Red (Nothing too bright!)
below header
http://www.brevicott.example
http://www.folmaneq.example/
http://4plank.example

```html
<!DOCTYPE html>
<html lang="en">
<head>
<meta charset="utf-8">
<title>Hallvard Veneer Technology</title>
<link href="https://fonts.googleapis.com/css2?family=Arimo:wght@400;700&display=swap" rel="stylesheet">
<style>
:root{
  --bg:#3b3b3b;
  --bg-dark:#2a2a2a;
  --panel:#242424;
  --panel-2:#4a4a4a;
  --brand-red:#c8161d;
  --text:#ffffff;
  --text-muted:#a9a9a9;
  --nav-grad-top:#5a5a5a;
  --nav-grad-bottom:#3a3a3a;
  --card-top:#5c5c5c;
  --card-bottom:#1f1f1f;
  --field:#ffffff;
}
*{margin:0;padding:0;box-sizing:border-box}
html,body{width:1200px;height:1014px;overflow:hidden}
body{background:var(--bg);font-family:"Arimo",Arial,sans-serif;color:var(--text);position:relative}
.header{position:absolute;left:0;top:0;width:1200px;height:200px;background:linear-gradient(var(--bg-dark),var(--bg))}
.brand{position:absolute;left:110px;top:20px;display:flex;align-items:center;gap:12px}
.brand-mark{width:60px;height:60px;background:var(--brand-red)}
.brand-name{font-size:30px;font-weight:700;color:var(--brand-red);line-height:1.05}
.tagline{position:absolute;left:378px;top:88px;font-size:30px;color:var(--text-muted)}
.search{position:absolute;left:748px;top:99px;display:flex;gap:6px}
.search-field{width:224px;height:24px;background:var(--field);border:1px solid #999}
.search-button{width:92px;height:24px;background:linear-gradient(#d8d8d8,#9a9a9a);color:#333;font-size:13px;text-align:center;line-height:24px;border-radius:2px}
.main-nav{position:absolute;left:99px;top:132px;width:1005px;height:60px;background:linear-gradient(var(--nav-grad-top),var(--nav-grad-bottom));display:flex;align-items:center;border-radius:4px 4px 0 0}
.main-nav a{color:var(--text);text-decoration:none;font-size:20px;width:170px;text-align:center;height:60px;line-height:60px}
.main-nav a.active{background:#fff;color:#222;width:156px}
.hero{position:absolute;left:99px;top:214px;width:1005px;height:252px;background:linear-gradient(100deg,#5b3a2a 0%,#c9b79a 30%,#e9e3d8 55%,#b48a66 75%,#8a2f28 100%);border-radius:4px}
.products-row{position:absolute;left:101px;top:485px;width:1003px;height:233px}
.card{position:absolute;top:0;height:233px;background:linear-gradient(var(--card-top),var(--card-bottom) 40%);border-radius:6px}
.card h3{font-size:21px;font-weight:400;text-align:center;margin-top:10px}
.card .thumb{display:block;margin:6px auto 0;width:178px;height:114px}
.card p{font-size:11.5px;line-height:15px;padding:8px 12px 0;color:#eee}
.card .more{position:absolute;right:14px;bottom:6px;background:#777;color:#eee;font-size:10px;padding:2px 6px}
.info-panel{position:absolute;left:99px;top:731px;width:676px;height:228px;background:var(--panel);border-radius:6px}
.info-col{position:absolute;top:18px}
.info-col h2{font-size:32px;font-weight:400;padding-bottom:6px;border-bottom:1px solid #777;width:200px}
.info-col ul{list-style:none;margin-top:12px}
.info-col li{font-size:18px;color:var(--text-muted);height:30px;display:flex;align-items:center;gap:14px}
.info-col li::before{content:"";width:9px;height:9px;border-radius:50%;border:2px solid #888}
.info-col li.current{color:var(--text)}
.info-col li.current::before{background:#fff;border-color:#fff}
.quote-panel{position:absolute;left:789px;top:731px;width:315px;height:228px;background:var(--panel-2);border-radius:6px;overflow:hidden}
.quote-panel h2{background:var(--panel);font-size:26px;font-weight:400;padding:10px 10px;height:50px}
.quote-row{display:flex;align-items:center;margin:14px 0 0 10px}
.quote-row label{width:91px;font-size:21px}
.quote-row .field{width:192px;height:26px;background:var(--field)}
.submit{position:absolute;right:20px;bottom:18px;width:82px;height:22px;background:linear-gradient(#eee,#aaa);color:#222;font-size:13px;text-align:center;line-height:22px;border-radius:3px}
.footer{position:absolute;left:0;top:973px;width:1200px;height:41px;background:var(--bg-dark);text-align:center;line-height:41px;font-size:15px}
</style>
</head>
<body>
<header class="header">
  <div class="brand"><span class="brand-mark"></span><span class="brand-name">Hallvard<br>Veneer Technology</span></div>
  <div class="tagline">...Designed By Nature</div>
  <div class="search"><div class="search-field"></div><div class="search-button">Search</div></div>
</header>
<nav class="main-nav">
  <a class="active" href="#">Home</a><a href="#">About Us</a><a href="#">Services</a><a href="#">Products</a><a href="#">Contact Us</a>
</nav>
<div class="hero" role="img" aria-label="Modern living room interior with fireplace, wood cabinetry and red sofa"></div>
<section class="products-row">
  <article class="card" style="left:0;width:244px"><h3>Stone-Veneer</h3><div class="thumb" role="img" aria-label="Stone veneer sheets" style="background:linear-gradient(135deg,#8a7d6a,#d8cbb3,#7a4a2e)"></div><p>It is a long established fact that a reader will be distracted by the readable content of a page when looking at its layout</p><span class="more">READ MORE</span></article>
  <article class="card" style="left:255px;width:233px"><h3>Sonic-Paneltrim</h3><div class="thumb" role="img" aria-label="Slatted wooden acoustic panel" style="background:linear-gradient(120deg,#5a3418,#c98a4a,#7a4a22)"></div><p>It is a long established fact that a reader will be distracted by the readable content of a page when looking at its layout</p><span class="more">READ MORE</span></article>
  <article class="card" style="left:505px;width:235px"><h3>Plexard</h3><div class="thumb" role="img" aria-label="Wall panel system installed in a room" style="background:linear-gradient(90deg,#c7b48a,#e8e2cf,#9bb0b8)"></div><p>It is a long established fact that a reader will be distracted by the readable content of a page when looking at its layout</p><span class="more">READ MORE</span></article>
  <article class="card" style="left:757px;width:246px"><h3>Moravelt</h3><div class="thumb" role="img" aria-label="Wooden acoustic slat panel" style="background:linear-gradient(135deg,#9a6a2e,#e0b070,#8a5a24)"></div><p>It is a long established fact that a reader will be distracted by the readable content of a page when looking at its layout</p><span class="more">READ MORE</span></article>
</section>
<section class="info-panel">
  <div class="info-col" style="left:24px"><h2>Navigation</h2><ul><li class="current">Home</li><li>News</li><li>Products</li><li>Corporate Social Responsibility</li><li>Contact Us</li></ul></div>
  <div class="info-col" style="left:394px"><h2>Products</h2><ul><li class="current">Stone-Veneer</li><li>Sonic-Paneltrim</li><li>Plexard</li><li>Moravelt</li></ul></div>
</section>
<section class="quote-panel">
  <h2>Get A Quote</h2>
  <div class="quote-row"><label>Name</label><div class="field"></div></div>
  <div class="quote-row"><label>Phone</label><div class="field"></div></div>
  <div class="quote-row"><label>Email</label><div class="field"></div></div>
  <div class="submit">Submit</div>
</section>
<footer class="footer">Copyright © Hallvard Veneer Technology,2010-2011</footer>
</body>
</html>
```